Simple and clean webdesign for personal homepage

Trying to create a simple and clean webdesign for my personal homepage. Going to use a static site builder with templates to build the site. I want it to have multiple pages - like an about me, blog and resume. I just need something very basic I can customize. I want the main colors to be purple, black and white. I am open to other color palettes too but since purple is my favorite color I want that to be one of the main colors.

The site be mostly text driven. Might have some images in the body text but I want the site design to be light and lean.

Industry/Entity Type

Personal Homepage.

Coding

Coded - Design and coding required

Number of Pages Required

1 page

Font styles to use
Sans Serif

Colors
6B429C
8869AF
B7A5CE
E3DAEB
F3F0F8

Requirements
Must have
• Clean design. Purple used as a color. HTML template.
Nice to have
• Responsive

```html
<!DOCTYPE html>
<html lang="en">
<head>
<meta charset="UTF-8">
<title>Personal Homepage</title>
<link href="https://fonts.googleapis.com/css2?family=Playfair+Display:wght@400;700&family=Poppins:wght@400&display=swap" rel="stylesheet">
<style>
:root{
  --purple-deep:#6B429C;
  --purple-mid:#8869AF;
  --purple-soft:#B7A5CE;
  --purple-pale:#E3DAEB;
  --purple-mist:#F3F0F8;
  --hero:#7A52AE;
  --frame:#D8BCF6;
  --white:#FFFFFF;
  --ink:#111111;
  --serif:'Playfair Display', Georgia, serif;
  --sans:'Poppins', Arial, sans-serif;
}
*{margin:0;padding:0;box-sizing:border-box}
html,body{width:1200px;height:3314px;overflow:hidden}
body{position:relative;background:var(--white);font-family:var(--sans);color:var(--ink)}
.abs{position:absolute}
.photo{position:absolute}

/* hero */
.hero{left:0;top:0;width:1200px;height:640px;background:linear-gradient(180deg,#7F55B3 0%,#7449A8 60%,#6E45A4 100%)}
.logo{left:168px;top:30px;font-family:var(--serif);font-weight:700;font-size:46px;color:var(--white);letter-spacing:.5px}
.main-nav{left:662px;top:42px;display:flex;gap:28px;font-family:var(--serif);font-size:24px;color:var(--white)}
.hero-title{left:172px;top:192px;width:520px;font-family:var(--serif);font-weight:700;font-size:60px;line-height:64px;color:var(--white)}
.hero-text{left:172px;top:344px;width:400px;font-size:19px;line-height:27px;color:var(--white)}
.btn-outline{left:172px;top:491px;width:227px;height:71px;border:2px solid var(--white);border-radius:0 36px 36px 0;display:flex;align-items:center;justify-content:center;font-family:var(--serif);font-weight:700;font-size:23px;color:var(--white)}
.hero-photo{left:714px;top:103px;width:334px;height:537px;background:linear-gradient(180deg,#A98CC9 0%,#EDE8F2 45%,#DAD3E2 100%);border-radius:160px 160px 0 0}

/* about */
.section-title{font-family:var(--serif);font-weight:700;font-size:52px;color:var(--purple-deep)}
.about-title{left:181px;top:702px}
.about-text{left:172px;top:783px;width:390px;font-size:19px;line-height:29.3px}
.btn-solid{left:174px;top:1078px;width:294px;height:78px;background:var(--purple-deep);border-radius:0 40px 40px 0;display:flex;align-items:center;justify-content:center;font-family:var(--serif);font-weight:700;font-size:19px;color:var(--white)}
.about-frame{left:620px;top:716px;width:407px;height:443px;background:var(--frame);border-radius:14px}
.about-photo{left:637px;top:733px;width:375px;height:408px;background:linear-gradient(135deg,#8A8F96 0%,#5B3591 55%,#3C3A40 100%);border-radius:8px}

/* mail list */
.mail-band{left:0;top:1245px;width:1200px;height:375px;background:linear-gradient(180deg,#B7A5CE 0%,#C2B2D6 60%,#B9A6CF 100%)}
.mail-title{left:0;top:1302px;width:1200px;text-align:center;font-family:var(--serif);font-weight:700;font-size:52px;color:var(--white)}
.mail-text{left:0;top:1390px;width:1200px;text-align:center;font-size:19px;line-height:30px;color:var(--white)}
.mail-form{left:284px;top:1479px;width:632px;height:55px;display:flex}
.mail-input{flex:1;background:var(--white);border-radius:28px 0 0 28px;padding-left:38px;display:flex;align-items:center;font-family:var(--serif);font-size:11px;color:var(--purple-deep)}
.mail-submit{width:180px;background:var(--purple-deep);border-radius:0 28px 28px 0;display:flex;align-items:center;justify-content:center;font-family:var(--serif);font-size:20px;color:var(--white)}

/* courses */
.courses-title{left:0;top:1683px;width:1200px;text-align:center}
.course-img-wide{left:174px;top:1789px;width:414px;height:176px;background:linear-gradient(90deg,#F1ECE6 0%,#C9BBAE 55%,#6E5A4C 100%)}
.course-img-a{left:174px;top:1987px;width:203px;height:176px;background:linear-gradient(180deg,#EDE2E6 0%,#C9A9BE 60%,#A985B3 100%)}
.course-img-b{left:383px;top:1987px;width:205px;height:176px;background:linear-gradient(135deg,#5C5049 0%,#B79A8A 50%,#E8DCD6 100%)}
.course{position:absolute}
.course h3{font-family:var(--serif);font-weight:700;font-size:25px;line-height:32px;color:var(--ink)}
.course p{font-size:19px;line-height:27px;margin-top:4px}
.read-more{display:inline-block;margin-top:10px;font-family:var(--serif);font-weight:700;font-size:19px;color:var(--purple-deep);border-bottom:2px solid var(--purple-deep);line-height:22px}
.course-main{left:622px;top:1780px;width:380px}
.course-a{left:622px;top:1980px;width:205px}
.course-b{left:840px;top:1980px;width:205px}

/* blog */
.blog-band{left:0;top:2292px;width:1200px;height:650px;background:linear-gradient(180deg,#E3DAEB 0%,#DCD0E8 50%,#E6DEEE 100%)}
.blog-title{left:0;top:2352px;width:1200px;text-align:center}
.post{position:absolute;top:2447px;width:275px;height:394px;background:var(--white)}
.post-img{position:absolute;left:0;top:0;width:100%;height:187px}
.post-date{position:absolute;left:61px;top:164px;width:152px;height:45px;border-radius:23px;background:var(--purple-deep);color:var(--white);font-size:19px;display:flex;align-items:center;justify-content:center}
.post h3{position:absolute;left:0;top:224px;width:100%;text-align:center;font-family:var(--serif);font-weight:700;font-size:19px;line-height:27px}
.post p{position:absolute;left:18px;top:292px;width:239px;text-align:center;font-size:14px;line-height:19.5px}
.post-1{left:170px}.post-2{left:463px}.post-3{left:752px}
.img-1{background:linear-gradient(135deg,#4A4642 0%,#B08F78 55%,#E7D6C8 100%)}
.img-2{background:linear-gradient(135deg,#8E7D6A 0%,#C9C7C2 55%,#6F6A66 100%)}
.img-3{background:linear-gradient(135deg,#3A3433 0%,#C7B5A6 55%,#EFE6DE 100%)}
.arrow{position:absolute;top:2627px;width:55px;height:55px}
.arrow-prev{left:73px}.arrow-next{left:1070px}

/* footer */
.footer{left:0;top:2942px;width:1200px;height:372px;background:linear-gradient(180deg,#8869AF 0%,#8A6BB2 100%)}
.footer-nav{left:0;top:3080px;width:1200px;display:flex;justify-content:center;gap:26px;font-family:var(--serif);font-size:30px;color:var(--white)}
.footer-nav span:nth-child(4){margin-left:8px}
.footer-nav span:nth-child(5){margin-left:8px}
.socials{left:421px;top:3156px;display:flex;gap:18px}
.social{width:56px;height:56px;border-radius:50%;background:var(--white)}
.copyright{left:0;top:3245px;width:1200px;text-align:center;font-family:var(--serif);font-size:16px;color:var(--white)}
</style>
</head>
<body>

<header class="abs hero">
</header>
<div class="abs logo">LOGO NAME</div>
<nav class="abs main-nav"><span>Home</span><span>About me</span><span>Blog</span><span>Resume</span></nav>
<h1 class="abs hero-title">Lorem ipsum dolor sit amet</h1>
<p class="abs hero-text">Lorem ipsum dolor sit amet, consectetur adipiscing elit, sed do eiusmod tempor incididunt ut labore et dolore magna aliqua.</p>
<div class="abs btn-outline">READ MORE</div>
<div class="photo hero-photo" role="img" aria-label="Portrait of a smiling woman with arms crossed, wearing a white shirt"></div>

<section>
  <h2 class="abs section-title about-title">ABOUT ME</h2>
  <p class="abs about-text">Lorem ipsum dolor sit amet, consectetur adipiscing elit, sed do eiusmod tempor incididunt ut labore et dolore magna aliqua. Ut enim ad minim veniam, quis nostrud exercitation ullamco laboris nisi ut aliquip ex ea commodo consequat.Duis aute irure dolor in reprehenderit in voluptate velit esse cillum dolore eu fugiat nulla pariatur.</p>
  <div class="abs btn-solid">DOWNLOAD MY RESUME</div>
  <div class="abs about-frame"></div>
  <div class="photo about-photo" role="img" aria-label="Woman in a purple sweater smiling at her phone beside a laptop"></div>
</section>

<section>
  <div class="abs mail-band" role="img" aria-label="Soft lavender field background with a person in the distance"></div>
  <h2 class="abs mail-title">MAIL LIST REGISTRATION</h2>
  <p class="abs mail-text">Lorem ipsum dolor sit amet, consectetur adipiscing elit, sed do eiusmod<br>tempor incididunt ut labore et dolore magna aliqua.</p>
  <div class="abs mail-form">
    <div class="mail-input">ENTER YOUR EMAIL</div>
    <div class="mail-submit">REGISTER NOW</div>
  </div>
</section>

<section>
  <h2 class="abs section-title courses-title">COURSES</h2>
  <div class="photo course-img-wide" role="img" aria-label="Hands typing on a laptop in soft daylight"></div>
  <div class="photo course-img-a" role="img" aria-label="Woman standing in a lavender field"></div>
  <div class="photo course-img-b" role="img" aria-label="Woman smiling at a desk with a laptop"></div>
  <div class="course course-main">
    <h3>Lorem ipsum dolor sit amet</h3>
    <p>Lorem ipsum dolor sit amet, consectetur adipiscing elit, sed do eiusmod tempor incididunt ut labore et dolore magna aliqua.</p>
    <span class="read-more">READ MORE</span>
  </div>
  <div class="course course-a">
    <h3>Lorem ipsumt</h3>
    <p>Lorem ipsum dolor amet, consectetur adipiscing elit, sed dolore magna aliqua.</p>
    <span class="read-more">READ MORE</span>
  </div>
  <div class="course course-b">
    <h3>Lorem ipsumt</h3>
    <p>Lorem ipsum dolor amet, consectetur adipiscing elit, sed dolore magna aliqua.</p>
    <span class="read-more">READ MORE</span>
  </div>
</section>

<section>
  <div class="abs blog-band" role="img" aria-label="Faded background of a woman among flowers"></div>
  <h2 class="abs section-title blog-title">BLOG</h2>
  <article class="post post-1">
    <div class="post-img img-1" role="img" aria-label="Hands typing on a laptop"></div>
    <div class="post-date">21-12-2021</div>
    <h3>Lorem Ipsum is dummy<br>typesetting industry.</h3>
    <p>Lorem Ipsum is simply dummy text of the printing and typesetting ever since the 1500s.</p>
  </article>
  <article class="post post-2">
    <div class="post-img img-2" role="img" aria-label="Person working on a laptop beside a wicker chair"></div>
    <div class="post-date">21-12-2021</div>
    <h3>Lorem Ipsum is dummy<br>typesetting industry.</h3>
    <p>Lorem Ipsum is simply dummy text of the printing and typesetting ever since the 1500s.</p>
  </article>
  <article class="post post-3">
    <div class="post-img img-3" role="img" aria-label="Woman holding a cup of coffee"></div>
    <div class="post-date">21-12-2021</div>
    <h3>Lorem Ipsum is dummy<br>typesetting industry.</h3>
    <p>Lorem Ipsum is simply dummy text of the printing and typesetting ever since the 1500s.</p>
  </article>
  <svg class="arrow arrow-prev" viewBox="0 0 55 55" aria-label="Previous">
    <circle cx="27.5" cy="27.5" r="26" fill="#6B429C" stroke="#fff" stroke-width="2"/>
    <path d="M31 17 L21 27.5 L31 38" fill="none" stroke="#fff" stroke-width="5" stroke-linecap="round" stroke-linejoin="round"/>
  </svg>
  <svg class="arrow arrow-next" viewBox="0 0 55 55" aria-label="Next">
    <circle cx="27.5" cy="27.5" r="26" fill="#6B429C" stroke="#fff" stroke-width="2"/>
    <path d="M24 17 L34 27.5 L24 38" fill="none" stroke="#fff" stroke-width="5" stroke-linecap="round" stroke-linejoin="round"/>
  </svg>
</section>

<footer>
  <div class="abs footer" role="img" aria-label="Faded background of a person with open arms"></div>
  <nav class="abs footer-nav"><span>Home</span><span>About me</span><span>Courses</span><span>Blog</span><span>Resume</span></nav>
  <div class="abs socials">
    <span class="social" aria-label="Social link 1"></span>
    <span class="social" aria-label="Social link 2"></span>
    <span class="social" aria-label="Social link 3"></span>
    <span class="social" aria-label="Social link 4"></span>
    <span class="social" aria-label="Social link 5"></span>
  </div>
  <p class="abs copyright">Copyright © 2022 Company name. All rights reserved.</p>
</footer>

</body>
</html>
```